Events Online Video Streaming Company

A website needs to be designed to replace the current website of a company that specialises in providing an online portal for streaming events to users. the current portal exists at: http://www.tazorin.com <- designers can get a "feel" for what they do and the content they require from this existing website.
the current tazorin logo and green color are to be maintined. i will upload an EPS of the logo soon.
The new design needs to highlight the main aspects of what they do: live streaming of events, multiple cameras, online chat, user activity data (like brindle metrics), customised front-ends.
we want the design to be in-between a corporate feel and modern, contemporary. ie. we dont want it to be too corporate (like the current website).
the design must also incorporate the word: fernoskaps as part of their slogan or sub-title.
hi everyone,

```html
<!DOCTYPE html>
<html lang="en">
<head>
<meta charset="utf-8">
<title>tazorin – Live Streaming of Events</title>
<link rel="stylesheet" href="https://fonts.googleapis.com/css2?family=Open+Sans:ital,wght@0,400;0,600;0,700;1,400;1,600&family=Roboto+Condensed:ital,wght@0,700;1,700&display=swap">
<style>
:root{
  --green:#8cc63f;
  --green-dark:#5f9a1e;
  --orange:#f26522;
  --charcoal:#2e2e2e;
  --ink:#3a3a3a;
  --muted:#9a9a9a;
  --card:#ececec;
  --white:#ffffff;
}
*{margin:0;padding:0;box-sizing:border-box}
html,body{width:871px;height:1200px;overflow:hidden;background:var(--white)}
body{position:relative;font-family:"Open Sans",Arial,sans-serif;color:var(--ink)}
.abs{position:absolute}

/* header */
.hero-bg{left:0;top:0;width:871px;height:445px}
.brand{left:143px;top:18px;font-size:40px;font-weight:400;color:var(--green);letter-spacing:.5px;line-height:48px}
.main-nav{left:311px;top:30px;width:560px;height:30px}
.main-nav a{position:absolute;top:0;height:30px;line-height:30px;font-size:10.5px;color:var(--white);text-decoration:none;white-space:nowrap}
.main-nav a.current{color:#222;font-weight:600}
.slogan-mark{left:538px;top:96px;font-family:"Roboto Condensed",Arial,sans-serif;font-style:italic;font-weight:700;font-size:48px;color:#474747;letter-spacing:.5px}
.hero-title{left:543px;top:170px;font-style:italic;font-weight:600;font-size:24px;line-height:27px;color:var(--green)}
.hero-copy{left:544px;top:228px;width:200px;font-size:8.6px;line-height:16px;color:#8a8a8a}
.tagline{left:186px;top:322px;font-style:italic;font-size:14px;color:var(--white);letter-spacing:.4px}
.service-label{top:393px;width:100px;text-align:center;font-size:10.5px;line-height:13px;color:var(--white)}

/* welcome */
.welcome{left:129px;top:410px;width:193px}
.welcome-line{position:relative;height:44.8px;border-bottom:2px dotted #cfcfcf;font-family:"Roboto Condensed",Arial,sans-serif;font-style:italic;font-weight:700;font-size:32px;line-height:44px;color:var(--ink);display:flex;align-items:center;gap:6px;white-space:nowrap}
.welcome-line .fill{flex:1;height:20px;background:#e6e6e6}
.welcome-line .accent{color:var(--green)}
.cta{left:129px;top:697px;width:193px;height:39px;border-radius:3px;background:linear-gradient(#9fd44e,#5f9a1e);color:var(--white);font-family:"Roboto Condensed",Arial,sans-serif;font-style:italic;font-weight:700;font-size:24px;line-height:39px;padding-left:10px;letter-spacing:.3px}

.benefit{width:170px}
.benefit svg{position:absolute;left:0;top:0}
.benefit h3{margin-left:37px;font-size:11px;font-weight:400;color:var(--ink);line-height:14px;white-space:nowrap}
.benefit p{margin-left:37px;margin-top:2px;width:128px;font-size:8.4px;line-height:11.6px;color:var(--muted);overflow:hidden;max-height:58px}
.benefit.tall p{max-height:81px}

/* features */
.rule{left:129px;width:607px;border-top:3px dotted #d6d6d6}
.section-title{left:129px;top:804px;font-size:18px;font-weight:600;color:var(--ink);letter-spacing:.3px}
.section-title span{color:var(--green)}
.feature-card{top:856px;width:137px;height:183px;background:var(--card)}
.feature-card.highlight{background:var(--white);border:2px solid var(--green);top:851px;height:190px}
.feature-card .thumb{position:absolute;left:3px;top:3px;width:131px;height:90px}
.feature-card.highlight .thumb{left:4px;top:12px;width:125px;height:86px}
.feature-card h4{position:absolute;left:6px;top:100px;font-size:10px;font-weight:400;color:#222;white-space:nowrap}
.feature-card.highlight h4{top:110px}
.feature-card p{position:absolute;left:6px;top:115px;width:126px;font-size:7.4px;line-height:9.6px;color:#666}
.feature-card.highlight p{top:125px}

/* footer */
.footer-bg{left:0;top:1083px;width:871px;height:117px}
.footer-links{top:1093px;list-style:none}
.footer-links li{font-size:8px;line-height:15.3px;color:var(--white)}
.footer-links li::before{content:"»";color:var(--green);margin-right:6px}
.follow{left:451px;top:1134px;font-size:8.5px;color:var(--white)}
.copyright{left:600px;top:1130px;font-size:9px;color:#222}
</style>
</head>
<body>

<svg class="abs hero-bg" viewBox="0 0 871 445" aria-hidden="true">
  <defs>
    <linearGradient id="heroShade" x1="0" y1="0" x2="1" y2="1">
      <stop offset="0" stop-color="#3b3b3b"/>
      <stop offset="1" stop-color="#262626"/>
    </linearGradient>
  </defs>
  <polygon points="92,0 871,0 871,445 404,445 316,350 128,350 121,99" fill="url(#heroShade)"/>
  <line x1="100" y1="48" x2="300" y2="340" stroke="#cfcfcf" stroke-width="1"/>
  <line x1="118" y1="70" x2="150" y2="110" stroke="#888" stroke-width="1"/>
  <polygon points="128,350 316,350 404,445 376,445 300,372 128,376" fill="#f26522"/>
  <polygon points="175,320 326,320 326,348 168,348" fill="#1f1f1f"/>
  <g fill="#ffffff">
    <circle cx="178" cy="363" r="11"/><circle cx="207" cy="363" r="11"/>
    <circle cx="236" cy="363" r="11"/><circle cx="265" cy="363" r="11"/>
    <circle cx="295" cy="363" r="11"/>
  </g>
  <polygon points="232,357 242,363 232,369" fill="#f26522"/>
  <g>
    <polygon points="437,338 464,365 437,392 410,365" fill="#8a8a8a"/>
    <polygon points="520,338 547,365 520,392 493,365" fill="#8cc63f"/>
    <polygon points="609,338 636,365 609,392 582,365" fill="#8cc63f"/>
    <polygon points="697,338 724,365 697,392 670,365" fill="#8cc63f"/>
  </g>
  <g fill="#ffffff">
    <rect x="427" y="356" width="20" height="15" rx="1"/>
    <rect x="509" y="358" width="15" height="12" rx="2"/><polygon points="524,361 532,357 532,371 524,367"/>
    <ellipse cx="605" cy="362" rx="10" ry="7"/><ellipse cx="614" cy="368" rx="8" ry="6"/>
    <rect x="690" y="355" width="3" height="20"/><rect x="695" y="357" width="12" height="3"/><rect x="695" y="363" width="8" height="3"/><rect x="695" y="369" width="14" height="3"/>
  </g>
</svg>

<svg class="abs" style="left:0;top:0" width="871" height="445" role="img" aria-label="Photo of presenters standing on a lit awards stage at a conference event">
  <defs>
    <linearGradient id="stageTone" x1="0" y1="0" x2="1" y2="1">
      <stop offset="0" stop-color="#7a2d40"/>
      <stop offset=".5" stop-color="#3f3560"/>
      <stop offset="1" stop-color="#6a2a3a"/>
    </linearGradient>
  </defs>
  <rect x="121" y="99" width="404" height="215" fill="url(#stageTone)"/>
</svg>

<svg class="abs" style="left:0;top:0" width="871" height="445" aria-hidden="true">
  <polygon points="0,60 121,99 121,314 240,314 0,0" fill="#ffffff" opacity="0"/>
  <g fill="none" stroke="#ffffff" stroke-width="2">
    <polyline points="196,294 191,300 196,306"/>
    <polyline points="256,294 261,300 256,306"/>
  </g>
  <g fill="none" stroke="#ffffff" stroke-width="1.5">
    <circle cx="208" cy="300" r="3.5" fill="#ffffff"/><circle cx="218" cy="300" r="3.5"/>
    <circle cx="228" cy="300" r="3.5"/><circle cx="238" cy="300" r="3.5"/><circle cx="248" cy="300" r="3.5"/>
  </g>
</svg>

<div class="abs brand">tazorin</div>

<svg class="abs" style="left:311px;top:30px" width="560" height="30" aria-hidden="true">
  <rect x="70" y="0" width="490" height="30" fill="#8cc63f"/>
  <polygon points="12,0 88,0 76,30 0,30" fill="#ffffff"/>
  <g stroke="#6aa52a" stroke-width="2">
    <line x1="147" y1="0" x2="135" y2="30"/><line x1="240" y1="0" x2="228" y2="30"/>
    <line x1="312" y1="0" x2="300" y2="30"/><line x1="380" y1="0" x2="368" y2="30"/>
  </g>
</svg>
<nav class="abs main-nav">
  <a class="current" href="#" style="left:25px">Home</a>
  <a href="#" style="left:86px">Features</a>
  <a href="#" style="left:157px">Applications</a>
  <a href="#" style="left:244px">The Team</a>
  <a href="#" style="left:315px">Support</a>
  <a href="#" style="left:385px">Contact</a>
</nav>

<div class="abs slogan-mark">fernoskaps</div>
<h1 class="abs hero-title">Live Streaming<br>of Events</h1>
<p class="abs hero-copy">Lorem Ipsum is simply dummy text of the printing and typesetting industry. Lorem Ipsum has been the industry's standard ...</p>
<div class="abs tagline">Social . Digital . Portal</div>

<div class="abs service-label" style="left:387px">Live streaming<br>of events</div>
<div class="abs service-label" style="left:470px">Multiple<br>cameras</div>
<div class="abs service-label" style="left:559px;top:401px">online chat</div>
<div class="abs service-label" style="left:653px">user activity<br>data</div>

<section class="abs welcome">
  <div class="welcome-line">WELCOME <span class="fill"></span></div>
  <div class="welcome-line">TO <span class="accent">TAZORIN</span><span class="fill"></span></div>
  <div class="welcome-line">A LIVE <span class="fill"></span></div>
  <div class="welcome-line">SOCIAL MEDIA</div>
  <div class="welcome-line">INTEGRATED <span class="fill"></span></div>
  <div class="welcome-line">PORTAL <span class="fill"></span></div>
</section>
<a class="abs cta">CONTACT US »</a>

<div class="abs benefit tall" style="left:368px;top:485px">
  <svg width="22" height="22" viewBox="0 0 20 20" aria-hidden="true"><circle cx="10" cy="9" r="5" fill="none" stroke="#8cc63f" stroke-width="2"/><rect x="8" y="14" width="4" height="4" fill="#8cc63f"/></svg>
  <h3>Innovation / Technology</h3>
  <p>Developments such as mobile devices, mobile internet, video streaming, cloud computing, and web development systems have made it possible for us to develop Tazorin with the use of the lastest innovative technologies.</p>
</div>
<div class="abs benefit tall" style="left:579px;top:485px">
  <svg width="24" height="22" viewBox="0 0 22 20" aria-hidden="true"><ellipse cx="8" cy="13" rx="7" ry="5" fill="#8cc63f"/><ellipse cx="14" cy="10" rx="7" ry="7" fill="#8cc63f"/></svg>
  <h3>Social Media, Networking</h3>
  <p>Users can engage with the event by integrating their existing social networking accounts allowing them to see their connections and establish professional relationships and discussion.</p>
</div>
<div class="abs benefit" style="left:368px;top:597px">
  <svg width="24" height="22" viewBox="0 0 22 20" aria-hidden="true"><rect x="0" y="6" width="14" height="11" rx="2" fill="#8cc63f"/><polygon points="14,9 21,5 21,18 14,14" fill="#8cc63f"/></svg>
  <h3>Live Video Streaming</h3>
  <p>High quality live video streaming means you get to see the event as it happens without waiting for a stream to buffer. Tazorin offers a choice of different resolutions to suit your</p>
</div>
<div class="abs benefit" style="left:579px;top:597px">
  <svg width="24" height="22" viewBox="0 0 22 20" aria-hidden="true"><rect x="1" y="8" width="19" height="11" fill="#8cc63f"/><polygon points="1,3 19,0 20,5 2,8" fill="#8cc63f"/></svg>
  <h3>Video on demand</h3>
  <p>Video on demand is available almost immediately after each session of the event, or as part of a media library so you can watch the video when ever you want.</p>
</div>
<div class="abs benefit" style="left:368px;top:699px">
  <svg width="22" height="24" viewBox="0 0 20 22" aria-hidden="true"><rect x="1" y="1" width="18" height="13" fill="#8cc63f"/><line x1="6" y1="14" x2="3" y2="21" stroke="#8cc63f" stroke-width="2"/><line x1="14" y1="14" x2="17" y2="21" stroke="#8cc63f" stroke-width="2"/><rect x="4" y="8" width="3" height="4" fill="#fff"/><rect x="9" y="5" width="3" height="7" fill="#fff"/></svg>
  <h3>Analytical reporting</h3>
  <p>Tazorin includes detailed reporting in realtime so you know who, when, where, why, how and for how long. You'll find out what works, and how to improve or tailor the content to make</p>
</div>
<div class="abs benefit" style="left:579px;top:699px">
  <svg width="22" height="26" viewBox="0 0 20 24" aria-hidden="true"><polygon points="7,0 13,0 11,4 15,20 10,24 5,20 9,4" fill="#8cc63f"/></svg>
  <h3>Sponsor/advertising</h3>
  <p>Tazorin is secure and allows event organisers to diversify their event income streams by adding revenue from virtual delegates as well as industry partners or</p>
</div>

<div class="abs rule" style="top:797px"></div>
<h2 class="abs section-title">OUR <span>FEATURES</span></h2>
<div class="abs rule" style="top:831px"></div>
<svg class="abs" style="left:692px;top:808px" width="44" height="18" aria-hidden="true">
  <g fill="none" stroke="#333" stroke-width="2"><polyline points="10,2 4,9 10,16"/><polyline points="34,2 40,9 34,16"/></g>
</svg>

<article class="abs feature-card" style="left:129px">
  <div class="thumb" role="img" aria-label="Photo of a padlock on a blue digital security background" style="background:linear-gradient(135deg,#0b2a4a,#2f7fb8,#0b2a4a)"></div>
  <h4>Secure event content</h4>
  <p>Tazorin allows event organisers to diversify their event income streams by adding revenue from virtual delegates as well as industry partners or sponsors of the event portal.</p>
</article>
<article class="abs feature-card" style="left:286px">
  <div class="thumb" role="img" aria-label="Photo of glowing blue technology lines over a row of screens" style="background:linear-gradient(180deg,#0a1a33,#2a6fb0,#0a1a33)"></div>
  <h4>Latest technology</h4>
  <p>Tazorin combines the very latest technologies into a portal that now makes it possible to attend an event online, while still getting many of the benefits of onsite attendance.</p>
</article>
<article class="abs feature-card highlight" style="left:442px">
  <svg class="abs" style="left:61px;top:-2px" width="14" height="9" aria-hidden="true"><polygon points="0,0 14,0 7,8" fill="#8cc63f"/></svg>
  <div class="thumb" role="img" aria-label="Photo of an audience seated in a conference hall" style="background:linear-gradient(135deg,#5a2a1c,#b2542e,#3a1a14)"></div>
  <h4>Too busy to attend?</h4>
  <p>With Tazorin you can stay at home or the office and fit the event into your schedule, your work, and your life without missing out.</p>
</article>
<article class="abs feature-card" style="left:597px">
  <div class="thumb" role="img" aria-label="Photo of a smiling group of business people" style="background:linear-gradient(135deg,#e8e4df,#9a8f86,#d9d4cf)"></div>
  <h4>Global audience</h4>
  <p>With Tazorin anyone in the world becomes a potential attendee, without the need to travel long distances at great expense.</p>
</article>

<svg class="abs footer-bg" viewBox="0 0 871 117" aria-hidden="true">
  <rect x="0" y="0" width="871" height="111" fill="#2a2a2a"/>
  <polygon points="670,0 871,0 871,111 736,111 736,55" fill="#ffffff"/>
  <polygon points="585,41 742,41 724,69 585,69" fill="#8cc63f"/>
  <rect x="0" y="111" width="871" height="6" fill="#8cc63f"/>
  <path d="M468,42 C470,22 495,15 512,28" fill="none" stroke="#ffffff" stroke-width="1.5"/>
  <polygon points="506,22 516,30 504,32" fill="#ffffff"/>
  <circle cx="522" cy="57" r="11" fill="#ffffff"/>
  <circle cx="549" cy="57" r="11" fill="#ffffff"/>
</svg>
<ul class="abs footer-links" style="left:135px">
  <li>Communications</li><li>Conferences and conventions</li><li>Education and training</li>
  <li>Festivals and Gigs</li><li>Live video streaming</li><li>Sporting Events</li>
</ul>
<ul class="abs footer-links" style="left:289px">
  <li>Welcome!</li><li>Features</li><li>Applications</li>
  <li>The Team</li><li>Support</li><li>Contact Us</li>
</ul>
<div class="abs follow">FOLLOW US:</div>
<div class="abs copyright">© Copyright 2013 - Tazorin</div>

</body>
</html>
```